Website banner

Here is the link where the current banner is featured https://www.brimlark.com.au/collections/gel-blasters

I need the banner recreated into desktop and mobile format size.
Update the key points to:
- FREE SHIPPING AUSTRALIA WIDE
- SAME DAY DISPATCH
- BEST PRICE GUARANTEE
- 3000+ 5 STAR REVIEWS
- BEST SERVICE & WARRANTY
- 100% SECURE CHECKOUT

I want the banner to suit the style of the website and make it look better than the last graphic.

I also need the "save even more" picture to be recreated as it looks very plain at the moment,

```html
<!DOCTYPE html>
<html lang="en">
<head>
<meta charset="utf-8">
<title>Brimlark – Why Shop With Us</title>
<link rel="stylesheet" href="https://fonts.googleapis.com/css2?family=Oswald:wght@500;600&display=swap">
<style>
  :root {
    --ink: #0b0b0b;
    --forest-mid: #3a3a3a;
    --forest-dark: #121212;
    --blood: #6f1416;
    --accent: #d5222a;
    --cream: #fbf0e6;
  }
  * { margin: 0; padding: 0; box-sizing: border-box; }
  html, body {
    width: 1200px; height: 766px; overflow: hidden;
    background: var(--ink);
  }
  .banner {
    position: relative; width: 1200px; height: 766px; overflow: hidden;
    font-family: "Oswald", "Arial Narrow", sans-serif;
    color: var(--cream);
  }
  .forest-backdrop {
    position: absolute; inset: 0;
    background:
      radial-gradient(ellipse 38% 55% at 52% 38%, #6a6a6a 0%, var(--forest-mid) 35%, transparent 75%),
      linear-gradient(180deg, var(--forest-dark) 0%, #262626 55%, #1a1a1a 80%, var(--ink) 100%);
  }
  .feature-art { position: absolute; }
  .splat { position: absolute; background: var(--blood); border-radius: 50%; }
  .art-placeholder {
    position: absolute;
    background: radial-gradient(ellipse at 50% 50%, #efe2d6 0%, #cfc2b6 100%);
    opacity: 0.9;
  }
  .caption {
    position: absolute; width: 360px; text-align: center;
    font-weight: 500; letter-spacing: -0.5px; text-transform: uppercase;
  }
  .caption .line { display: block; font-size: 34px; line-height: 42px; }
  .caption .hl {
    display: inline-block; background: var(--accent); color: var(--cream);
    padding: 0 3px; font-size: 40px; line-height: 42px; font-weight: 600;
  }
  .caption sup { font-size: 18px; vertical-align: 14px; }
  .col-left  { left: 20px; }
  .col-mid   { left: 420px; }
  .col-right { left: 816px; }
  .row-top    { top: 226px; }
  .row-bottom { top: 603px; }
</style>
</head>
<body>
<main class="banner">
  <div class="forest-backdrop" role="img" aria-label="Dark misty pine forest photograph"></div>

  <!-- Free shipping -->
  <div class="splat" role="img" aria-label="Blood splatter with a map of Australia marked with dotted lines" style="left:88px;top:28px;width:200px;height:196px;"></div>
  <p class="caption col-left row-top">
    <span class="line"><span class="hl">Free</span> Shipping</span>
    <span class="line">Australia Wide</span>
  </p>

  <!-- Same day dispatch -->
  <svg class="feature-art" style="left:546px;top:66px" width="110" height="110" viewBox="0 0 110 110" aria-hidden="true">
    <polygon fill="var(--cream)" points="22,0 110,0 110,88 96,88 96,24 12,108 2,98 86,14 22,14"/>
  </svg>
  <p class="caption col-mid row-top">
    <span class="line"><span class="hl">Same</span> Day</span>
    <span class="line">Dispatch</span>
  </p>

  <!-- Best price -->
  <div class="splat" role="img" aria-label="Diagonal blood splash" style="left:830px;top:50px;width:310px;height:180px;border-radius:40% 60% 45% 55%;transform:rotate(-35deg);"></div>
  <svg class="feature-art" style="left:945px;top:66px" width="110" height="86" viewBox="0 0 110 86" aria-hidden="true">
    <polyline points="8,40 40,72 102,8" fill="none" stroke="var(--cream)" stroke-width="16"/>
  </svg>
  <p class="caption col-right row-top">
    <span class="line">Best Price</span>
    <span class="line"><span class="hl">Guarantee</span></span>
  </p>

  <!-- Reviews -->
  <div class="art-placeholder" role="img" aria-label="Illustration of a row of five star badges" style="left:52px;top:437px;width:296px;height:92px;border-radius:46px;"></div>
  <p class="caption col-left row-bottom">
    <span class="line"><span class="hl">3000<sup>+</sup></span></span>
    <span class="line">5 Star Reviews</span>
  </p>

  <!-- Service -->
  <div class="splat" role="img" aria-label="Spray-paint blood splatter" style="left:470px;top:385px;width:244px;height:200px;border-radius:48% 52% 46% 54%;"></div>
  <svg class="feature-art" style="left:522px;top:406px" width="156" height="156" viewBox="0 0 156 156" aria-hidden="true">
    <path d="M138,72 A60,60 0 1 0 78,136" fill="none" stroke="var(--cream)" stroke-width="12"/>
    <rect x="128" y="62" width="22" height="34" rx="6" fill="var(--cream)"/>
    <rect x="66" y="128" width="34" height="16" rx="8" fill="var(--cream)"/>
  </svg>
  <p class="caption col-mid row-bottom">
    <span class="line">Best <span class="hl">Service</span></span>
    <span class="line">&amp; Warranty</span>
  </p>

  <!-- Secure checkout -->
  <div class="art-placeholder" role="img" aria-label="Illustration of a key entering a secure frame" style="left:906px;top:418px;width:186px;height:154px;border-radius:6px;"></div>
  <p class="caption col-right row-bottom">
    <span class="line"><span class="hl">100%</span> Secure</span>
    <span class="line">Checkout</span>
  </p>
</main>
</body>
</html>
```